Business Card Design Project

We need a new business card design that will allow us to incorporate three different logos. All three logos fall under our corporate name, Voltaro, Inc. Our current business card only has one logo on it. We have logo for our mobile printer division, a logo for our dot-matrix division, and a logo for our custom solutions division. I'd like all three logos to be on the new business card. I'd like the business card to have the same color scheme as our corporate web site: www.voltaro-example.com. We are a technology company that manufactures dot-matrix and mobile thermal printer. We also do custom OEM products as well.

Industry/Entity Type

Printer

Requirements
Must have
• all three logos on the business card

```html
<!DOCTYPE html>
<html lang="en">
<head>
<meta charset="utf-8">
<title>Voltaro, Inc. – Business Card</title>
<link rel="stylesheet" href="https://fonts.googleapis.com/css2?family=Arimo:wght@400;700&display=swap">
<style>
  :root {
    --brand-blue: #1a8bd0;
    --deep-blue: #1560a8;
    --ink: #111111;
    --paper: #ffffff;
    --stage: #e6e7e9;
    --muted: #3a3a3a;
  }
  * { box-sizing: border-box; margin: 0; padding: 0; }
  html, body { width: 1200px; height: 900px; overflow: hidden; }
  body {
    background: var(--stage);
    font-family: "Arimo", Arial, sans-serif;
    position: relative;
  }
  .card {
    position: absolute;
    top: 302px;
    width: 520px;
    height: 297px;
    background: var(--paper);
    overflow: hidden;
    box-shadow: 0 6px 18px rgba(0,0,0,0.18);
  }
  .card--front { left: 60px; }
  .card--back { left: 620px; }

  /* front */
  .brand-primary {
    position: absolute; left: 30px; top: 26px;
    font-weight: 700; font-size: 34px; letter-spacing: 1px;
    color: var(--deep-blue);
  }
  .divisions {
    position: absolute; left: 30px; top: 78px;
    display: flex; gap: 34px; align-items: center;
  }
  .division {
    display: flex; align-items: center; gap: 6px;
    font-weight: 700; font-size: 14px; color: var(--ink);
  }
  .division--solutions { color: var(--deep-blue); }
  .division-mark { width: 11px; height: 11px; background: currentColor; }
  .contact { position: absolute; left: 30px; top: 122px; color: var(--muted); }
  .contact-name { font-size: 15px; color: var(--brand-blue); letter-spacing: 0.5px; }
  .contact-title { font-size: 10px; margin-top: 3px; }
  .contact-address { font-size: 11px; margin-top: 12px; }
  .contact-lines { font-size: 11px; margin-top: 8px; line-height: 1.4; }
  .label { color: var(--brand-blue); }
  .contact-web { font-size: 13px; color: var(--brand-blue); }
  .front-band {
    position: absolute; left: 0; bottom: 0; width: 100%; height: 34px;
  }

  /* back */
  .back-brand {
    position: absolute; left: 22px; top: 16px;
    font-weight: 700; font-size: 30px; letter-spacing: 1px;
    color: var(--deep-blue);
  }
  .back-band {
    position: absolute; left: 0; top: 66px; width: 100%; height: 96px;
    background: var(--brand-blue);
  }
  .back-mobile {
    position: absolute; left: 170px; top: 86px;
    font-weight: 700; font-size: 30px; line-height: 1; color: var(--ink);
    display: flex; align-items: center; gap: 12px;
  }
  .back-mobile .division-mark { width: 26px; height: 26px; }
  .back-solutions {
    position: absolute; left: 22px; top: 178px;
    font-weight: 700; font-size: 40px; line-height: 1.05; color: var(--ink);
  }
  .circuit-art {
    position: absolute; right: 22px; top: 20px; width: 118px; height: 40px;
    background: linear-gradient(90deg, #cfcfcf, #4a4a4a);
  }
</style>
</head>
<body>
  <section class="card card--front" aria-label="Business card front">
    <div class="brand-primary">VOLTARO</div>
    <div class="divisions">
      <div class="division division--mobile"><span class="division-mark"></span>VOLTARO MOBILE</div>
      <div class="division division--solutions"><span class="division-mark"></span>Voltaro Custom Solutions</div>
    </div>
    <div class="contact">
      <div class="contact-name">DANIEL MERCER</div>
      <div class="contact-title">Manager</div>
      <div class="contact-address">4820 Harbor Crest Way, Lakeview, FL 34500</div>
      <div class="contact-lines">
        <div><span class="label">Ph:</span> (800) 555-0142 <span class="label">Fax:</span> (269) 555-0187</div>
        <div><span class="label">email:</span> info@voltaro-example.com</div>
        <div class="contact-web">www.voltaro-example.com</div>
      </div>
    </div>
    <svg class="front-band" viewBox="0 0 520 34" preserveAspectRatio="none" aria-hidden="true">
      <rect x="0" y="0" width="520" height="34" fill="var(--brand-blue)"/>
      <polygon points="420,0 520,0 520,34 400,34" fill="var(--ink)"/>
    </svg>
  </section>

  <section class="card card--back" aria-label="Business card back">
    <div class="back-brand">VOLTARO</div>
    <div class="circuit-art" role="img" aria-label="Circuit-trace decoration of lines ending in dots"></div>
    <div class="back-band"></div>
    <div class="back-mobile"><span class="division-mark"></span>VOLTARO MOBILE</div>
    <div class="back-solutions">Voltaro<br>Custom Solutions</div>
  </section>
</body>
</html>
```